Internet service provider (ISP) flyer

Added Sep 8 - updated content language in brief below
Added Sep 8 - testimonials:

5 star rating on Voxelpeak
5 star rating on NorthlinkRate
"Unparalleled speeds, unlimited bandwith, amazing prices, immediate local customer service."
"Multiple Streamvue streams without issue"
"Fantastic for gaming. Very low ping..."
(End of testimonials)

--

We are looking for a 1/2 page double sided flyer to advertise our internet packages.

We provide Internet phone and TV services to residents living in condo buildings only.

Here is the content:

(Big heading must be on front)

Unlimited Fast Internet
Starting at $35 monthly

(Rest of content placement up to you)

(3 packages)

Fibre50 $35 monthly
50 Mbps download and upload speed
Unlimited Internet usage

Fibre250 $55 monthly
250 Mbps download and upload speed
Unlimited Internet usage

Fibre500 $75 monthly
500 Mbps download and upload speed
Unlimited Internet Usage

Gigabit Upgrade
LumaWire technicians built a gigabit fibre network in your building

No modems
Use your own wireless router or purchase from us.

No Contracts
Cancel any time, no notice required.

Local Support
Our team is located in Toronto and Ottawa

--

HD TELEVISION - add TV packages from $18 monthly

HOME PHONE - add Home Phone from $20 monthly

(our guarantee)

All LumaWire services include a risk free 30-day money back guarantee.

(contact information)

Your local sales rep:

Hank
(555) 482-3907
hank@lumawire-example.ca

Since 2009
Lumawire-example.ca
(555) 630-4418

Target Market(s)

Young professionals

Industry/Entity Type

Telecommunications

Font styles to use
Sans Serif
Other font styles liked:
• Roboto or Century Gothic

Colors
000000
f37122
acd136
757575

Requirements
Must have
• Front page that grabs attention
• Professional looking design
• Internet that looks fast
Nice to have
• Advanced fibre look and feel
• Dark / black background
• See attached images for look and feel samples
Should not have
• No cheesy corporate stock
• No images from our website

```html
<!DOCTYPE html>
<html lang="en">
<head>
<meta charset="utf-8">
<title>LumaWire – Unlimited Fast Internet</title>
<link rel="stylesheet" href="https://fonts.googleapis.com/css2?family=Questrial&display=swap">
<style>
  :root {
    --page: #ffffff;
    --ink: #000000;
    --orange: #f37122;
    --orange-deep: #b8560f;
    --amber: #f6a52c;
    --lime: #c9ea4c;
    --rating: #f4b73a;
    --grey: #757575;
  }
  * { margin: 0; padding: 0; box-sizing: border-box; }
  html, body {
    width: 1200px; height: 900px; overflow: hidden;
    background: var(--page);
  }
  .flyer {
    position: absolute; left: 285px; top: 0;
    width: 638px; height: 900px;
    background: var(--ink);
    overflow: hidden;
    font-family: "Questrial", "Century Gothic", sans-serif;
  }
  .flyer__shapes { position: absolute; inset: 0; }
  .flyer__text { position: absolute; white-space: nowrap; line-height: 1; }

  .brand { left: 40px; top: 22px; font-size: 38px; color: var(--orange); letter-spacing: -0.5px; }

  .headline { color: var(--lime); letter-spacing: 1px; }
  .headline--main { left: 60px; top: 112px; font-size: 84px; }
  .headline--sub { left: 64px; top: 216px; font-size: 58px; }

  .offer { color: var(--orange); }
  .offer--lead { left: 37px; top: 318px; font-size: 35px; letter-spacing: 1px; }
  .offer--price { left: 60px; top: 366px; font-size: 54px; letter-spacing: 1px; }

  .rating { color: var(--rating); font-size: 27px; letter-spacing: 0.5px; }
  .rating--one { left: 158px; top: 550px; }
  .rating--two { left: 175px; top: 576px; }

  .contact { color: var(--amber); letter-spacing: 0.5px; }
  .contact--title { left: 140px; top: 678px; font-size: 25px; }
  .contact--line { font-size: 20px; }
  .contact--tel { left: 98px; top: 742px; word-spacing: 3px; }
  .contact--tel span { margin-left: 30px; }
  .contact--email { left: 80px; top: 773px; }
  .contact--web { left: 57px; top: 805px; }
  .since { left: 158px; top: 868px; font-size: 25px; color: var(--orange); letter-spacing: 0.5px; }
</style>
</head>
<body>
<main class="flyer">
  <svg class="flyer__shapes" width="638" height="900" viewBox="0 0 638 900">
    <defs>
      <linearGradient id="streak-band" x1="0" y1="0" x2="1" y2="0.4">
        <stop offset="0" stop-color="#e8600f"/>
        <stop offset="0.5" stop-color="#f58a22"/>
        <stop offset="1" stop-color="#f9c640"/>
      </linearGradient>
      <linearGradient id="highway-glow" x1="0" y1="0" x2="0.4" y2="1">
        <stop offset="0" stop-color="#1a1206"/>
        <stop offset="0.35" stop-color="#5a3a10"/>
        <stop offset="0.7" stop-color="#a8400c"/>
        <stop offset="1" stop-color="#d2611a"/>
      </linearGradient>
    </defs>
    <g class="streak-band" role="img" aria-label="Orange light-streak motion blur band">
      <polygon points="0,0 635,0 448,303 0,303" fill="url(#streak-band)"/>
      <rect class="brand-plate" x="0" y="0" width="315" height="75" fill="var(--orange-deep)" opacity="0.75"/>
      <polygon points="0,75 130,75 0,290" fill="var(--ink)"/>
    </g>
    <polygon class="highway-photo" role="img" aria-label="Night highway with long-exposure orange and white light trails"
      points="0,303 415,303 638,580 638,620 450,900 0,900 0,888 150,600 0,303" fill="url(#highway-glow)"/>
    <polyline class="next-arrow" points="603,430 633,457 603,484" fill="none" stroke="var(--orange)" stroke-width="3"/>
  </svg>

  <div class="flyer__text brand">LumaWire</div>

  <h1 class="flyer__text headline headline--main">UNLIMITED</h1>
  <div class="flyer__text headline headline--sub">FAST INTERNET</div>

  <div class="flyer__text offer offer--lead">Starting at</div>
  <div class="flyer__text offer offer--price">$35 monthly</div>

  <div class="flyer__text rating rating--one">5 star rating on Voxelpeak</div>
  <div class="flyer__text rating rating--two">5 star rating on NorthlinkRate</div>

  <div class="flyer__text contact contact--title">CONTACT US :</div>
  <div class="flyer__text contact contact--line contact--tel">TEL: (555) 482-3907<span>(555) 630-4418</span></div>
  <div class="flyer__text contact contact--line contact--email">EMAIL: hank@lumawire-example.ca</div>
  <div class="flyer__text contact contact--line contact--web">www.Lumawire-example.ca</div>

  <div class="flyer__text since">Since 2009</div>
</main>
</body>
</html>
```